New Business Card Design Project

Target Market(s)

Passing cards out

Industry/Entity Type

Asphalt contractor

Contact Information for Business Card

Ridgefold Paving

Colors
FFC000
F8CF3A
FAE287
FDF2CF
FEFAEE
F0912C
F2A743
F7CA91
FBE8D2
FDF5EE
EE7325
F08F49
F5BC92
FAE3D3
FDF4ED

Requirements
Must have
• Asphalt
Nice to have
• Would like to have 2 pictures on it of equipment

```html
<!DOCTYPE html>
<html lang="en">
<head>
<meta charset="utf-8">
<title>Ridgefold Paving – Business Card</title>
<link rel="stylesheet" href="https://fonts.googleapis.com/css2?family=Anton&family=Montserrat:wght@400;500;600;700&family=Allura&display=swap">
<style>
  :root{
    --backdrop:#c2a27b;
    --card:#f7f6f4;
    --ink:#222222;
    --ink-soft:#3a3a3a;
    --red:#e11b22;
    --orange:#f07c17;
    --asphalt-dark:#3f4148;
    --asphalt-light:#a6a9b0;
    --truck-yellow:#e8a51f;
    --truck-grey:#8d8f92;
  }
  *{margin:0;padding:0;box-sizing:border-box}
  html,body{width:697px;height:1200px;overflow:hidden}
  body{background:var(--backdrop);position:relative;font-family:"Montserrat",sans-serif;color:var(--ink)}
  .card{position:absolute;left:48px;width:600px;height:343px;background:var(--card);
        box-shadow:0 14px 22px rgba(0,0,0,.22);overflow:hidden}
  .card--front{top:220px}
  .card--back{top:620px}
  .photo{position:absolute;border-radius:40% 50% 45% 40%}
  .photo--road-top{left:14px;top:0;width:130px;height:108px;
        background:linear-gradient(150deg,var(--asphalt-light),var(--asphalt-dark))}
  .photo--road-bottom{left:150px;top:230px;width:125px;height:113px;border-radius:50% 45% 0 0;
        background:linear-gradient(200deg,var(--asphalt-light),var(--asphalt-dark))}
  .brand{position:absolute;left:38px;top:128px;width:230px;display:flex;align-items:center;gap:8px}
  .brand__dot{width:16px;height:16px;border-radius:50%;background:var(--red);flex:none}
  .brand__name{font-family:"Anton",sans-serif;font-size:30px;line-height:1;color:var(--red);letter-spacing:.5px}
  .pitch{position:absolute;left:300px;top:36px;width:290px}
  .script{font-family:"Allura",cursive;color:var(--red)}
  .pitch__tag{font-size:32px;line-height:.9}
  .pitch__head{font-family:"Anton",sans-serif;font-size:28px;line-height:1.18;color:var(--ink);text-transform:uppercase}
  .pitch__head .hot{color:var(--orange)}
  .services{position:absolute;left:300px;top:158px;font-size:16.5px;line-height:26px;color:var(--ink-soft)}
  .phones{position:absolute;left:300px;top:256px;list-style:none}
  .phones li{display:flex;align-items:center;gap:10px;font-size:19px;font-weight:500;line-height:29px}
  .phones svg{width:12px;height:12px;fill:var(--red)}
  .names{position:absolute;left:38px;top:32px;font-size:31px;font-weight:700;line-height:40px;color:var(--orange)}
  .motto{position:absolute;left:38px;top:148px;font-size:27px;font-weight:500;color:var(--ink)}
  .since{position:absolute;left:38px;top:182px;display:flex;align-items:baseline;gap:10px}
  .since__word{font-size:52px;line-height:1}
  .since__year{font-family:"Anton",sans-serif;font-size:44px;color:var(--ink);line-height:1}
  .email{position:absolute;left:38px;top:290px;display:flex;align-items:center;gap:10px;font-size:17px;font-weight:500}
  .email svg{width:20px;height:14px}
  .photo--truck-top{left:350px;top:0;width:205px;height:150px;border-radius:12px;
        background:linear-gradient(135deg,var(--truck-yellow),#6d5a3f 70%,#2e2e30)}
  .photo--truck-bottom{left:345px;top:155px;width:240px;height:178px;border-radius:12px;
        background:linear-gradient(135deg,#2e2e30,var(--truck-grey) 45%,#d9d9d9)}
</style>
</head>
<body>
  <section class="card card--front">
    <div class="photo photo--road-top" role="img" aria-label="Winding strip of cracked asphalt"></div>
    <div class="photo photo--road-bottom" role="img" aria-label="Winding strip of cracked asphalt"></div>
    <div class="brand">
      <span class="brand__dot"></span>
      <span class="brand__name">RIDGEFOLD PAVING</span>
    </div>
    <div class="pitch">
      <div class="script pitch__tag">Do it Right</div>
      <div class="pitch__head">Speacialist in <span class="hot">Chipseal</span><br>&amp; <span class="hot">Hotmix</span></div>
    </div>
    <div class="services">
      Ranch Roads | City Streets<br>
      Sub Divisions | Patching<br>
      Driveways | Parking Lots
    </div>
    <ul class="phones">
      <li><svg viewBox="0 0 24 24"><path d="M6.6 10.8a15.1 15.1 0 0 0 6.6 6.6l2.2-2.2a1 1 0 0 1 1-.25 11.4 11.4 0 0 0 3.6.57 1 1 0 0 1 1 1V20a1 1 0 0 1-1 1A17 17 0 0 1 3 4a1 1 0 0 1 1-1h3.5a1 1 0 0 1 1 1c0 1.25.2 2.45.57 3.57a1 1 0 0 1-.25 1z"/></svg>903 555 0148</li>
      <li><svg viewBox="0 0 24 24"><path d="M6.6 10.8a15.1 15.1 0 0 0 6.6 6.6l2.2-2.2a1 1 0 0 1 1-.25 11.4 11.4 0 0 0 3.6.57 1 1 0 0 1 1 1V20a1 1 0 0 1-1 1A17 17 0 0 1 3 4a1 1 0 0 1 1-1h3.5a1 1 0 0 1 1 1c0 1.25.2 2.45.57 3.57a1 1 0 0 1-.25 1z"/></svg>903 555 0192</li>
    </ul>
  </section>

  <section class="card card--back">
    <div class="names">WADE CARTER<br>COLT CARTER</div>
    <div class="motto">DO IT RIGHT</div>
    <div class="since">
      <span class="script since__word">Since</span>
      <span class="since__year">1992</span>
    </div>
    <div class="email">
      <svg viewBox="0 0 20 14"><rect width="20" height="14" rx="1.5" fill="#e11b22"/><path d="M1 1.5 10 8l9-6.5" fill="none" stroke="#f7f6f4" stroke-width="1.6"/></svg>
      ridgefoldpaving@mail.com
    </div>
    <div class="photo photo--truck-top" role="img" aria-label="Yellow dump truck with trailer loaded with asphalt"></div>
    <div class="photo photo--truck-bottom" role="img" aria-label="Grey dump truck loaded with asphalt"></div>
  </section>
</body>
</html>
```